Verdane Training Center
Golf Simulation & Character Education
Corporate
Milo Raskett
Chief Operations Officer
Brisby Center
North Charleston, SC
Milo@verdanetrainingcenter.com
verdanetrainingcenter.com
I would like for my logo design to be incorporated into the card design
logo full size of card on the back

```html
<!DOCTYPE html>
<html lang="en">
<head>
<meta charset="UTF-8">
<title>Verdane Training Center – Business Card</title>
<link href="https://fonts.googleapis.com/css2?family=Open+Sans:wght@400;700&display=swap" rel="stylesheet">
<style>
  :root {
    --backdrop: #d9d9d9;
    --card: #ffffff;
    --brand-red: #8e1b1b;
    --ink: #1c1c1c;
    --text-gray: #4a4a4a;
    --rule: #c8c8c8;
  }
  * { margin: 0; padding: 0; box-sizing: border-box; }
  html, body {
    width: 1200px;
    height: 864px;
    overflow: hidden;
    background: var(--backdrop);
    font-family: "Open Sans", Arial, sans-serif;
  }
  .card {
    position: absolute;
    left: 100px;
    top: 146px;
    width: 1000px;
    height: 572px;
    background: var(--card);
    border-radius: 36px;
    box-shadow: 0 6px 22px rgba(0,0,0,0.18);
  }
  .brand {
    position: absolute;
    left: 56px;
    top: 250px;
    width: 330px;
    display: flex;
    align-items: center;
    gap: 18px;
  }
  .brand-dot {
    flex: none;
    width: 54px;
    height: 54px;
    border-radius: 50%;
    background: var(--brand-red);
  }
  .brand-name {
    color: var(--brand-red);
    font-weight: 700;
    font-size: 30px;
    line-height: 1.15;
  }
  .holder {
    position: absolute;
    left: 446px;
    top: 58px;
  }
  .holder-name {
    color: var(--brand-red);
    font-weight: 700;
    font-size: 38px;
    line-height: 1.1;
  }
  .holder-title {
    color: var(--ink);
    font-weight: 700;
    font-size: 20px;
    margin-top: 4px;
  }
  .divider {
    position: absolute;
    left: 440px;
    top: 168px;
    width: 1px;
    height: 280px;
    background: var(--rule);
  }
  .address {
    position: absolute;
    left: 470px;
    top: 178px;
    color: var(--text-gray);
    font-size: 21px;
    line-height: 1.3;
  }
  .contacts {
    position: absolute;
    left: 462px;
    top: 322px;
    list-style: none;
    color: var(--text-gray);
    font-size: 21px;
  }
  .contacts li {
    display: flex;
    align-items: center;
    gap: 14px;
    height: 40px;
  }
  .contacts svg {
    width: 22px;
    height: 22px;
    flex: none;
  }
</style>
</head>
<body>
  <section class="card">
    <div class="brand">
      <span class="brand-dot"></span>
      <span class="brand-name">Verdane<br>Training Center</span>
    </div>

    <header class="holder">
      <h1 class="holder-name">Milo Raskett</h1>
      <p class="holder-title">Chief Operations Officer</p>
    </header>

    <div class="divider"></div>

    <address class="address">
      Brisby Center<br>
      North Charleston,<br>
      SC 29406
    </address>

    <ul class="contacts">
      <li>
        <svg viewBox="0 0 24 24" aria-hidden="true">
          <rect x="7" y="2" width="10" height="20" rx="2" fill="none" stroke="#8e1b1b" stroke-width="2"/>
          <line x1="10" y1="18" x2="14" y2="18" stroke="#8e1b1b" stroke-width="2"/>
        </svg>
        <span>843-555-0172</span>
      </li>
      <li>
        <svg viewBox="0 0 24 24" aria-hidden="true">
          <circle cx="12" cy="12" r="4" fill="none" stroke="#8e1b1b" stroke-width="2"/>
          <path d="M16 8v5a3 3 0 0 0 6 0v-1a10 10 0 1 0-4 8" fill="none" stroke="#8e1b1b" stroke-width="2"/>
        </svg>
        <span>Milo@verdanetrainingcenter.com</span>
      </li>
      <li>
        <svg viewBox="0 0 24 24" aria-hidden="true">
          <circle cx="12" cy="12" r="9.5" fill="none" stroke="#8e1b1b" stroke-width="2"/>
          <ellipse cx="12" cy="12" rx="4" ry="9.5" fill="none" stroke="#8e1b1b" stroke-width="1.6"/>
          <line x1="2.5" y1="12" x2="21.5" y2="12" stroke="#8e1b1b" stroke-width="1.6"/>
        </svg>
        <span>www.verdanetrainingcenter.com</span>
      </li>
    </ul>
  </section>
</body>
</html>
```